LUMO Company Folder Design Color

I am looking for someone who can create a company folder design. L.U.M.O. Enterprises is a consulting firm, we assist business owner in their journeys to success. The design should be professional and mus include some inspirational words. I like elegance and modern. The colors red, white and black should be used. The design should look conservative, but not too serious. I do not like english or Times New Roman letters.

Target Market(s)

Healthcare Providers

Industry/Entity Type

Business

Colors
ec1f27
ffffff

Requirements
Must have
• color red and words like knowledge, success, confidence

```html
<!DOCTYPE html>
<html lang="en">
<head>
<meta charset="utf-8">
<title>L.U.M.O. Enterprises – Company Folder</title>
<link rel="stylesheet" href="https://fonts.googleapis.com/css2?family=Jost:wght@400;500&display=swap">
<style>
  :root {
    --backdrop: #242425;
    --charcoal: #3a3a3c;
    --charcoal-deep: #2c2c2e;
    --charcoal-edge: #4a4a4c;
    --red: #ec1f27;
    --red-deep: #d81920;
    --red-light: #f2555a;
    --white: #ffffff;
    --ink-soft: #e6e6e6;
  }
  * { box-sizing: border-box; margin: 0; padding: 0; }
  html, body { width: 1200px; height: 900px; overflow: hidden; }
  body {
    background: var(--backdrop);
    font-family: "Jost", "Helvetica Neue", Arial, sans-serif;
    position: relative;
  }
  .folder-shapes { position: absolute; inset: 0; }

  .brand {
    position: absolute;
    display: flex;
    flex-direction: column;
    align-items: center;
    color: var(--red);
    font-weight: 400;
    text-align: center;
  }
  .brand__dot {
    width: 62px; height: 62px;
    border-radius: 50%;
    background: var(--red);
    margin-bottom: 10px;
  }
  .brand__name { font-size: 22px; line-height: 1.1; letter-spacing: 0.5px; }
  .brand__tagline { font-size: 15px; line-height: 1.2; }

  .brand--back { left: 300px; top: 388px; width: 240px; }
  .brand--front { left: 808px; top: 268px; width: 188px; }
  .brand--front .brand__dot { width: 48px; height: 48px; margin-bottom: 8px; }
  .brand--front .brand__name { font-size: 19px; }
  .brand--front .brand__tagline { font-size: 13px; }

  .contact {
    position: absolute;
    left: 244px; top: 558px;
    color: var(--ink-soft);
    font-size: 10px;
    list-style: none;
  }
  .contact__heading { margin-bottom: 8px; }
  .contact__item { display: flex; align-items: center; gap: 8px; margin-bottom: 6px; }
  .contact__item svg { width: 12px; height: 12px; fill: var(--ink-soft); }

  .slogan {
    position: absolute;
    left: 637px; top: 636px;
    color: var(--white);
    font-size: 27px;
    font-weight: 400;
    letter-spacing: 0.6px;
  }
</style>
</head>
<body>
  <svg class="folder-shapes" width="1200" height="900" viewBox="0 0 1200 900" aria-hidden="false">
    <defs>
      <linearGradient id="backPanel" x1="0" y1="0" x2="1" y2="1">
        <stop offset="0" stop-color="var(--charcoal-edge)"/>
        <stop offset="0.5" stop-color="var(--charcoal)"/>
        <stop offset="1" stop-color="var(--charcoal-deep)"/>
      </linearGradient>
      <radialGradient id="frontPanel" cx="0.6" cy="0.3" r="0.8">
        <stop offset="0" stop-color="var(--red-light)"/>
        <stop offset="0.55" stop-color="var(--red)"/>
        <stop offset="1" stop-color="var(--red-deep)"/>
      </radialGradient>
    </defs>

    <!-- pocket tab -->
    <polygon class="pocket-tab" points="150,600 232,600 232,792 176,792 150,770" fill="var(--charcoal-deep)"/>
    <!-- back cover -->
    <rect class="back-cover" x="228" y="88" width="372" height="708" fill="url(#backPanel)"/>
    <!-- front cover, red area with decorative tiles -->
    <rect class="front-cover-art" x="600" y="100" width="400" height="605" fill="url(#frontPanel)"
          role="img" aria-label="Abstract pattern of tilted white tiles on red"/>
    <!-- white lower band with diagonal pocket edge -->
    <polygon class="front-pocket" points="496,800 600,705 1000,705 1000,815 600,815" fill="var(--white)"/>
    <!-- logo box -->
    <rect class="front-logo-box" x="800" y="255" width="200" height="150" fill="var(--white)"/>
  </svg>

  <div class="brand brand--back">
    <span class="brand__dot"></span>
    <span class="brand__name">L.U.M.O. Enterprises</span>
    <span class="brand__tagline">Healthcare Consulting</span>
  </div>

  <ul class="contact">
    <li class="contact__heading">Address Line goes here:</li>
    <li class="contact__item">
      <svg viewBox="0 0 24 24"><path d="M6.6 10.8a15 15 0 0 0 6.6 6.6l2.2-2.2c.3-.3.7-.4 1-.2 1.1.4 2.3.6 3.6.6.6 0 1 .4 1 1V20c0 .6-.4 1-1 1A17 17 0 0 1 3 4c0-.6.4-1 1-1h3.5c.6 0 1 .4 1 1 0 1.3.2 2.5.6 3.6.1.3 0 .7-.2 1z"/></svg>
      123 456 7890
    </li>
    <li class="contact__item">
      <svg viewBox="0 0 24 24"><path d="M12 2a10 10 0 1 0 0 20 10 10 0 0 0 0-20zm6.9 6h-3a15 15 0 0 0-1.3-3.9A8 8 0 0 1 18.9 8zM12 4c.8 1.2 1.5 2.5 1.9 4h-3.8c.4-1.5 1.1-2.8 1.9-4zM4.3 14a8 8 0 0 1 0-4h3.4a16 16 0 0 0 0 4zm.8 2h3a15 15 0 0 0 1.3 3.9A8 8 0 0 1 5.1 16zm3-8h-3a8 8 0 0 1 4.3-3.9A15 15 0 0 0 8.1 8zM12 20c-.8-1.2-1.5-2.5-1.9-4h3.8c-.4 1.5-1.1 2.8-1.9 4zm2.3-6H9.7a14 14 0 0 1 0-4h4.6a14 14 0 0 1 0 4zm.3 5.9a15 15 0 0 0 1.3-3.9h3a8 8 0 0 1-4.3 3.9zm1.7-5.9a16 16 0 0 0 0-4h3.4a8 8 0 0 1 0 4z"/></svg>
      www.dummytext.com
    </li>
    <li class="contact__item">
      <svg viewBox="0 0 24 24"><path d="M2 5h20v14H2zm2 2v.5l8 5 8-5V7zm0 2.8V17h16V9.8l-8 5z"/></svg>
      info@dummymail.com
    </li>
  </ul>

  <div class="brand brand--front">
    <span class="brand__dot"></span>
    <span class="brand__name">L.U.M.O. Enterprises</span>
    <span class="brand__tagline">Healthcare Consulting</span>
  </div>

  <p class="slogan">ALWAYS THERE FOR YOU</p>
</body>
</html>
```